Business card design

I need my logo on this card, things I need the card to have on it
licensed and insured.
owner operators Derek & Milton Halvorsen
my phone number 5418237906
Disaster Recovery, Storm Damage Restoration, Proactive Disaster Plan Management, Roof Repair/Restoration Structural Repair and Reconstruction, Emergency Boarding and Tarping Service, Perimeter Fencing, Emergency Tree Removal,

```html
<!DOCTYPE html>
<html lang="en">
<head>
<meta charset="utf-8">
<title>Halvorsen's Construction L.L.C – Business Card</title>
<link rel="stylesheet" href="https://fonts.googleapis.com/css2?family=Fira+Sans:wght@400&family=Questrial&display=swap">
<style>
  :root {
    --backdrop: #d3d4d6;
    --card: #ffffff;
    --brand-blue: #3a8fd3;
    --mark-fill: #d9e6f2;
    --text-grey: #555a60;
  }
  * { box-sizing: border-box; margin: 0; padding: 0; }
  html, body {
    width: 900px; height: 1200px; overflow: hidden;
    background: var(--backdrop);
  }
  .canvas { position: relative; width: 900px; height: 1200px; }
  .card {
    position: absolute; width: 633px; height: 364px;
    background: var(--card);
  }
  .card--front { left: 133px; top: 210px; }
  .card--back { left: 134px; top: 624px; }

  .brand-mark {
    position: absolute; background: var(--mark-fill);
  }
  .card--front .brand-mark { left: 120px; top: 106px; width: 94px; height: 94px; }
  .card--back .brand-mark { left: 460px; top: 30px; width: 78px; height: 78px; }

  .brand-name {
    position: absolute; text-align: center;
    font-family: "Questrial", sans-serif; font-weight: 400;
    color: var(--brand-blue);
  }
  .card--front .brand-name {
    left: 40px; top: 214px; width: 255px;
    font-size: 23px; line-height: 26px;
  }
  .card--back .brand-name {
    left: 393px; top: 116px; width: 212px;
    font-size: 19px; line-height: 22px;
  }

  .services { position: absolute; left: 330px; top: 46px; font-family: "Fira Sans", sans-serif; }
  .services__title {
    font-size: 17px; font-weight: 400; color: var(--brand-blue);
    letter-spacing: 0.3px; margin-bottom: 12px;
  }
  .services__list { list-style: none; }
  .services__item {
    position: relative; padding-left: 20px;
    font-size: 14px; line-height: 22.5px; color: var(--text-grey);
    letter-spacing: 0.2px; margin-bottom: 7.5px;
  }
  .services__icon { position: absolute; left: 0; top: 4px; width: 13px; height: 12px; }

  .licence {
    position: absolute; right: 28px; top: 166px;
    font-family: "Questrial", sans-serif; font-size: 15px;
    letter-spacing: 1.6px; color: var(--text-grey);
  }
  .owners { position: absolute; left: 29px; top: 218px; font-family: "Questrial", sans-serif; }
  .owners__names { font-size: 20px; font-weight: 400; color: var(--brand-blue); letter-spacing: 0.3px; }
  .owners__role { font-size: 15px; color: var(--text-grey); letter-spacing: 1px; margin-top: 5px; }
  .contact { list-style: none; margin-top: 12px; }
  .contact__item {
    display: flex; align-items: center; gap: 6px;
    font-size: 15px; color: var(--text-grey); line-height: 23px; letter-spacing: 0.4px;
  }
  .contact__item--phone { letter-spacing: 1.6px; }
  .contact__icon { width: 15px; height: 15px; flex: none; }
</style>
</head>
<body>
<div class="canvas">

  <section class="card card--front">
    <div class="brand-mark" role="img" aria-label="Company logo symbol"></div>
    <p class="brand-name">Halvorsen's<br>Construction L.L.C</p>

    <div class="services">
      <h2 class="services__title">OUR SERVICES:</h2>
      <ul class="services__list">
        <li class="services__item"><svg class="services__icon" viewBox="0 0 13 12"><path d="M0 5L6.5 0L13 5V12H0Z" fill="var(--brand-blue)"/><rect x="2.5" y="6" width="3" height="6" fill="#fff"/><rect x="7.5" y="6" width="3" height="3" fill="#fff"/></svg>Disaster Recovery</li>
        <li class="services__item"><svg class="services__icon" viewBox="0 0 13 12"><path d="M0 5L6.5 0L13 5V12H0Z" fill="var(--brand-blue)"/><rect x="2.5" y="6" width="3" height="6" fill="#fff"/><rect x="7.5" y="6" width="3" height="3" fill="#fff"/></svg>Storm Damage Restoration</li>
        <li class="services__item"><svg class="services__icon" viewBox="0 0 13 12"><path d="M0 5L6.5 0L13 5V12H0Z" fill="var(--brand-blue)"/><rect x="2.5" y="6" width="3" height="6" fill="#fff"/><rect x="7.5" y="6" width="3" height="3" fill="#fff"/></svg>Proactive Disaster Plan Management</li>
        <li class="services__item"><svg class="services__icon" viewBox="0 0 13 12"><path d="M0 5L6.5 0L13 5V12H0Z" fill="var(--brand-blue)"/><rect x="2.5" y="6" width="3" height="6" fill="#fff"/><rect x="7.5" y="6" width="3" height="3" fill="#fff"/></svg>Roof Repair/Restoration Structural<br>Repair and Reconstruction</li>
        <li class="services__item"><svg class="services__icon" viewBox="0 0 13 12"><path d="M0 5L6.5 0L13 5V12H0Z" fill="var(--brand-blue)"/><rect x="2.5" y="6" width="3" height="6" fill="#fff"/><rect x="7.5" y="6" width="3" height="3" fill="#fff"/></svg>Emergency Boarding and<br>Tarping Service</li>
        <li class="services__item"><svg class="services__icon" viewBox="0 0 13 12"><path d="M0 5L6.5 0L13 5V12H0Z" fill="var(--brand-blue)"/><rect x="2.5" y="6" width="3" height="6" fill="#fff"/><rect x="7.5" y="6" width="3" height="3" fill="#fff"/></svg>Perimeter Fencing</li>
        <li class="services__item"><svg class="services__icon" viewBox="0 0 13 12"><path d="M0 5L6.5 0L13 5V12H0Z" fill="var(--brand-blue)"/><rect x="2.5" y="6" width="3" height="6" fill="#fff"/><rect x="7.5" y="6" width="3" height="3" fill="#fff"/></svg>Emergency Tree Removal</li>
      </ul>
    </div>
  </section>

  <section class="card card--back">
    <div class="brand-mark" role="img" aria-label="Company logo symbol"></div>
    <p class="brand-name">Halvorsen's<br>Construction L.L.C</p>
    <p class="licence">LICENSED AND INSURED</p>

    <div class="owners">
      <h1 class="owners__names">Derek &amp; Milton Halvorsen</h1>
      <p class="owners__role">Owner Operator</p>
      <ul class="contact">
        <li class="contact__item contact__item--phone">
          <svg class="contact__icon" viewBox="0 0 24 24"><path d="M6.6 10.8a15.1 15.1 0 0 0 6.6 6.6l2.2-2.2a1 1 0 0 1 1-.25 11.4 11.4 0 0 0 3.6.57 1 1 0 0 1 1 1V20a1 1 0 0 1-1 1A17 17 0 0 1 3 4a1 1 0 0 1 1-1h3.5a1 1 0 0 1 1 1c0 1.25.2 2.45.57 3.57a1 1 0 0 1-.25 1z" fill="var(--brand-blue)"/></svg>
          5418237906
        </li>
        <li class="contact__item">
          <svg class="contact__icon" viewBox="0 0 24 24"><rect x="1" y="5" width="22" height="14" fill="var(--brand-blue)"/><path d="M1 5l11 8 11-8" fill="none" stroke="#fff" stroke-width="1.6"/></svg>
          info@halvorsenconstructionllc.com
        </li>
        <li class="contact__item">
          <svg class="contact__icon" viewBox="0 0 24 24" fill="none" stroke="var(--brand-blue)" stroke-width="1.6"><circle cx="12" cy="12" r="10"/><ellipse cx="12" cy="12" rx="4.5" ry="10"/><path d="M2 12h20M4 6.5h16M4 17.5h16M12 2v20"/></svg>
          halvorsenconstructionllc.com
        </li>
      </ul>
    </div>
  </section>

</div>
</body>
</html>
```